Modern Can & Tray Design Competition

Please note our brand is now called zé, please do not submit any entries with the wording or logo of "zé kelpwater". Read the full design brief below before making an entry, please.

A competition to design can packaging and outer tray designs for a new exciting brand.

See examples of the design assets I want, below, including both a can and outer tray:

1. https://quillmarketgoods.eu/beverages/energy-drinks/vomba-boost-the-amber-edition-12-x-025-liter-cans-nl/?lang=en

2. https://www.plimvo.com/nl/nl/p/tarvo-fizz-cherry-slim-cans-24-x-330-ml-eu/4812000077312904/

We have 2 flavours in our range, so we need two separate can designs and a separate outer tray design for each flavour.

Our drinks are currently packaged in PET plastic bottles. Our flavours are:
Lemon & Lime - https://zekelpwater.co.uk/products/lemon-and-lime
Strawberry - https://zekelpwater.co.uk/products/strawberry

For this competition, I want can designs for each flavour in 250ml style cans like used by Vomba. And I also want an outer tray for the cans designed for each flavour. Our brand is changing to “zé” so please do not use “kelpwater” on any part of the design. The logo should be “zé” and for each flavour the ze should show the fruit for the flavour embedded inside it. See the files called “ze_fruit_logo_LEMLI (1)” and “ze_fruit_logo_STR (1)” for what I mean. You can use these files for your design.

Under the logo it should state on the can “Prebiotic Fibre Drink”. Similar to how VomBa has “Energy Drink” written under its logo: https://www.drenvilo.com/wp-content/uploads/2009/11/vomba-can-250ml-1.jpg

If you can submit your design ideas for this competition with a picture of the can next to the tray like this for each flavour, that will be best: https://img.keltoshop.com/images/I/57qTzWa2pLx._SL1500_.jpg

So, two design concepts/ideas are needed to enter: One for Lemon & Lime and one for Strawberry.

We want vibrant, eye-catching packaging designs that will catch the consumer's attention.

Right now, we have ze in the centre of our packaging design with fruit embedded in the ze. This must remain a key part of your design as mentioned above. Also, as we will be launching other drinks as a company under different brand names and to unify our different brands we want a splash effect on all the cans which will be replicated across our other brands. So, please have some kind of splash effect on each flavour that can be replicated on the cans of our other brands in future.

Design considerations:

There is also certain information we need on the front/face of the can.

On the very top of the can just below the neck and above the logo we want it to state: “Supports Gut & Overall health*” example: https://pmkgrocerhub.co.uk/wp-content/uploads/2023/10/Brova-Zest-Lemonade.jpg

We also want the number of calories to be stated somewhere on the can in a clever way like in a droplet of the water splash effect. The number of the calories is “17 kcals”.

Under the ze logo as mentioned we want the wording: “Prebiotic Fibre Drink”

Then under Prebiotic Fibre Drink we want the name of the flavour - and then under the flavour we want 3 features stated. Which are:

“20% of daily fibre”
“0g sugar”
“Nothing artificial“

This could be laid out as 3 circles with icons or some other way. The last piece of information under these 3 features is then the size of the can “250 mle”.

In terms of “feel” of the design we want a vibrant colourful feel, and it should show pictures of fruit on it. Here is an example
https://gardenhollowtonics.com/wp-content/uploads/sites/2/2023/03/GHT-US-SodaRange-%E2%80%93-bb-1220x883.png

Any questions let me know. I look forward to seeing your ideas.

To see more about our brand, view our website: www.zekelpwater.co.uk

```html
<!DOCTYPE html>
<html lang="en">
<head>
<meta charset="utf-8">
<title>zé Prebiotic Fibre Drink – Can Labels</title>
<link href="https://fonts.googleapis.com/css2?family=Poppins:wght@500;600;700;800&display=swap" rel="stylesheet">
<style>
  :root {
    --page-bg: #f8f3f3;
    --straw-base: #e3173a;
    --straw-deep: #c8102e;
    --straw-glow: #fbd3da;
    --straw-ink: #ffffff;
    --straw-accent: #e8123a;
    --straw-fruit: #d81e2c;
    --straw-fruit-light: #f2604f;
    --lime-base: #bcd86a;
    --lime-deep: #9cc53f;
    --lime-glow: #f8f39a;
    --lime-ink: #3f6b1c;
    --lime-logo: #5fae1f;
    --lime-fruit: #8cc63f;
    --lemon-fruit: #f6e23a;
    --kcal-straw: #e8122f;
    --kcal-lime: #f7ec2a;
  }
  * { box-sizing: border-box; margin: 0; padding: 0; }
  html, body {
    width: 900px; height: 1200px; overflow: hidden;
    background: var(--page-bg);
    font-family: "Poppins", sans-serif;
  }
  .range {
    display: flex; gap: 24px; justify-content: center;
    padding-top: 100px;
  }
  .label {
    position: relative;
    width: 428px; height: 1000px;
    overflow: hidden;
  }
  .label--strawberry {
    background:
      radial-gradient(ellipse 60% 32% at 50% 44%, var(--straw-glow) 0%, rgba(251,211,218,0.6) 40%, rgba(227,23,58,0) 100%),
      var(--straw-base);
    color: var(--straw-ink);
  }
  .label--lemon-lime {
    background:
      radial-gradient(ellipse 65% 35% at 50% 50%, var(--lime-glow) 0%, rgba(248,243,154,0.7) 45%, rgba(188,216,106,0) 100%),
      var(--lime-base);
    color: var(--lime-ink);
  }
  .waves { position: absolute; inset: 0; width: 100%; height: 100%; }

  .claim {
    position: absolute; top: 22px; left: 0; right: 0;
    text-align: center; font-weight: 700; font-size: 19px; letter-spacing: 0.3px;
  }
  .photo { position: absolute; }
  .photo--cluster { left: 0; top: 64px; width: 150px; height: 120px; border-radius: 50% 55% 45% 40%; }
  .photo--slice { right: 10px; top: 82px; width: 160px; height: 110px; border-radius: 50%; transform: rotate(-18deg); }
  .photo--drop { left: 236px; top: 206px; width: 86px; height: 92px; border-radius: 50% 50% 45% 45%; }
  .photo--halves { left: 86px; top: 690px; width: 256px; height: 135px; border-radius: 48% 48% 50% 50%; }

  .label--strawberry .photo { background: radial-gradient(circle at 40% 40%, var(--straw-fruit-light), var(--straw-fruit) 70%); }
  .label--lemon-lime .photo--cluster { background: radial-gradient(circle at 50% 45%, #fff6a0, var(--lemon-fruit) 70%); }
  .label--lemon-lime .photo--slice { background: radial-gradient(circle, #e9f7b0 0%, var(--lime-fruit) 70%); }
  .label--lemon-lime .photo--drop { background: radial-gradient(circle at 40% 35%, #8fd24a, #3f9a1e 75%); }
  .label--lemon-lime .photo--halves { background: linear-gradient(90deg, var(--lime-fruit), #d8ee7a 45%, var(--lemon-fruit)); }

  .kcal {
    position: absolute; left: 40px; top: 208px;
    width: 88px; height: 88px; border-radius: 50%;
    display: flex; flex-direction: column; align-items: center; justify-content: center;
    font-weight: 800; line-height: 0.9;
  }
  .kcal__num { font-size: 33px; }
  .kcal__unit { font-size: 24px; }
  .label--strawberry .kcal { background: var(--kcal-straw); color: #fff; }
  .label--lemon-lime .kcal { background: var(--kcal-lime); color: var(--lime-ink); }

  .brand-mark {
    position: absolute; left: 0; right: 0; top: 250px;
    text-align: center; font-weight: 800; font-size: 300px; line-height: 1; letter-spacing: -6px;
  }
  .label--strawberry .brand-mark { color: var(--straw-accent); }
  .label--lemon-lime .brand-mark { color: var(--lime-logo); }

  .product-type { position: absolute; left: 0; right: 0; top: 595px; text-align: center; line-height: 1; }
  .product-type__main { display: block; font-weight: 800; font-size: 58px; letter-spacing: 0.5px; }
  .product-type__sub { display: block; font-weight: 800; font-size: 30px; margin-top: -2px; letter-spacing: 0.5px; }
  .label--strawberry .product-type { color: var(--straw-accent); }
  .label--lemon-lime .product-type { color: var(--lime-ink); }

  .flavour {
    position: absolute; left: 0; right: 0; top: 830px;
    text-align: center; font-weight: 700; font-size: 30px; letter-spacing: 4px;
  }
  .features {
    position: absolute; left: 30px; right: 30px; top: 880px;
    display: flex; justify-content: space-between; list-style: none;
  }
  .feature { width: 110px; text-align: center; font-weight: 500; font-size: 15px; line-height: 1.05; }
  .feature svg { display: block; margin: 0 auto 4px; width: 46px; height: 46px; }
  .size {
    position: absolute; left: 0; right: 0; top: 950px;
    text-align: center; font-weight: 600; font-size: 30px;
  }
</style>
</head>
<body>
<main class="range">

  <section class="label label--strawberry" aria-label="zé Strawberry can label">
    <svg class="waves" viewBox="0 0 428 1000" aria-hidden="true">
      <path d="M0 150 C70 120 140 180 220 150 C300 120 360 170 428 140 L428 0 L0 0 Z" fill="#e3173a"/>
      <path d="M0 150 C70 120 140 180 220 150 C300 120 360 170 428 140" fill="none" stroke="#f3a3b2" stroke-width="10" opacity="0.6"/>
      <path d="M0 760 C80 720 160 790 240 750 C320 710 380 760 428 730 L428 800 L0 800 Z" fill="#f06a82" opacity="0.5"/>
      <path d="M0 800 L428 800 L428 1000 L0 1000 Z" fill="#e3173a"/>
    </svg>
    <p class="claim">SUPPORTS GUT &amp; OVERALL HEALTH</p>
    <div class="photo photo--cluster" role="img" aria-label="Whole strawberries with leaves"></div>
    <div class="photo photo--slice" role="img" aria-label="Halved strawberry"></div>
    <div class="photo photo--drop" role="img" aria-label="Strawberry droplet"></div>
    <div class="kcal"><span class="kcal__num">17</span><span class="kcal__unit">kcals</span></div>
    <p class="brand-mark">zé</p>
    <h2 class="product-type"><span class="product-type__main">PREBIOTIC</span><span class="product-type__sub">FIBRE DRINK</span></h2>
    <div class="photo photo--halves" role="img" aria-label="Two strawberry halves"></div>
    <p class="flavour">STRAWBERRY</p>
    <ul class="features">
      <li class="feature">
        <svg viewBox="0 0 48 48" fill="none" stroke="currentColor" stroke-width="3"><circle cx="24" cy="24" r="5" fill="currentColor"/><circle cx="10" cy="12" r="4"/><circle cx="38" cy="12" r="4"/><circle cx="10" cy="36" r="4"/><circle cx="38" cy="36" r="4"/><circle cx="24" cy="6" r="3"/><path d="M13 15 L20 21 M35 15 L28 21 M13 33 L20 27 M35 33 L28 27 M24 9 L24 19"/></svg>
        20% of<br>Daily Fibre</li>
      <li class="feature">
        <svg viewBox="0 0 48 48" fill="none" stroke="currentColor" stroke-width="3"><circle cx="24" cy="24" r="20"/><rect x="15" y="16" width="12" height="12"/><rect x="21" y="22" width="12" height="12"/><path d="M10 38 L38 10"/></svg>
        0g sugar</li>
      <li class="feature">
        <svg viewBox="0 0 48 48" fill="none" stroke="currentColor" stroke-width="3"><path d="M8 40 C8 18 22 8 42 6 C40 28 30 40 8 40 Z"/><path d="M8 40 L30 18 M18 30 L18 22 M24 24 L31 24"/></svg>
        Nothing<br>Artificial</li>
    </ul>
    <p class="size">250 ml</p>
  </section>

  <section class="label label--lemon-lime" aria-label="zé Lemon &amp; Lime can label">
    <svg class="waves" viewBox="0 0 428 1000" aria-hidden="true">
      <path d="M0 160 C70 130 140 190 220 160 C300 130 360 180 428 150 L428 0 L0 0 Z" fill="#bcd86a"/>
      <path d="M0 160 C70 130 140 190 220 160 C300 130 360 180 428 150" fill="none" stroke="#e2ef9e" stroke-width="10" opacity="0.7"/>
      <path d="M0 760 C80 720 160 790 240 750 C320 710 380 760 428 730 L428 800 L0 800 Z" fill="#a9cf4c" opacity="0.6"/>
      <path d="M0 800 L428 800 L428 1000 L0 1000 Z" fill="#bcd86a"/>
    </svg>
    <p class="claim">SUPPORTS GUT &amp; OVERALL HEALTH</p>
    <div class="photo photo--cluster" role="img" aria-label="Lemon slices with mint leaves"></div>
    <div class="photo photo--slice" role="img" aria-label="Lime slice with leaf"></div>
    <div class="photo photo--drop" role="img" aria-label="Whole lime"></div>
    <div class="kcal"><span class="kcal__num">17</span><span class="kcal__unit">kcals</span></div>
    <p class="brand-mark">zé</p>
    <h2 class="product-type"><span class="product-type__main">PREBIOTIC</span><span class="product-type__sub">FIBRE DRINK</span></h2>
    <div class="photo photo--halves" role="img" aria-label="Lime and lemon slices with leaves"></div>
    <p class="flavour">LEMON &amp; LIME</p>
    <ul class="features">
      <li class="feature">
        <svg viewBox="0 0 48 48" fill="none" stroke="currentColor" stroke-width="3"><circle cx="24" cy="24" r="5" fill="currentColor"/><circle cx="10" cy="12" r="4"/><circle cx="38" cy="12" r="4"/><circle cx="10" cy="36" r="4"/><circle cx="38" cy="36" r="4"/><circle cx="24" cy="6" r="3"/><path d="M13 15 L20 21 M35 15 L28 21 M13 33 L20 27 M35 33 L28 27 M24 9 L24 19"/></svg>
        20% of<br>Daily Fibre</li>
      <li class="feature">
        <svg viewBox="0 0 48 48" fill="none" stroke="currentColor" stroke-width="3"><circle cx="24" cy="24" r="20"/><rect x="15" y="16" width="12" height="12"/><rect x="21" y="22" width="12" height="12"/><path d="M10 38 L38 10"/></svg>
        0g sugar</li>
      <li class="feature">
        <svg viewBox="0 0 48 48" fill="none" stroke="currentColor" stroke-width="3"><path d="M8 40 C8 18 22 8 42 6 C40 28 30 40 8 40 Z"/><path d="M8 40 L30 18 M18 30 L18 22 M24 24 L31 24"/></svg>
        Nothing<br>Artificial</li>
    </ul>
    <p class="size">250 ml</p>
  </section>

</main>
</body>
</html>
```